Creative Challenge - Disruptive Digital Construction Business needs an Application Design

We need an application design (4 screens).
The app will offer easy-to-use an interactive course to illustrate the latest technology to construction professionals. Kindly find the attachments.
Updates

I have just posted the contest and the deadline is tomorrow!! Please give me my original 7 days back.

Need extra days to review

Target Market(s)

Construction professionals, aged from 22 to 36, who want to learn new disruptive technologies in construction.

Colors
e667a6
b868aa
33a6d7

Requirements
Must have
• The name of the app, Velmiro, stands for “Virtual Engineering Leaders”. The user is a Velmiro, who would transform the digital construction industry. We want a design that gives that feel to the users.

```html
<!DOCTYPE html>
<html lang="en">
<head>
<meta charset="utf-8">
<title>Velmiro – App Screens</title>
<link href="https://fonts.googleapis.com/css2?family=Roboto:wght@400;500;700&display=swap" rel="stylesheet">
<style>
:root{
  --pink:#e667a6;
  --purple:#b868aa;
  --blue:#33a6d7;
  --ink:#1f2340;
  --muted:#8d909c;
  --icon:#5567c9;
  --screen:#f3f4f6;
  --field:#e6e7ea;
  --track:#d6d8de;
  --frame:#161616;
  --grad:linear-gradient(90deg,var(--purple),var(--blue));
}
*{box-sizing:border-box;margin:0;padding:0}
html,body{width:1200px;height:476px;overflow:hidden;background:#fff;font-family:'Roboto',sans-serif;color:var(--ink)}
.stage{position:relative;width:2560px;height:1015px;transform:scale(.46875);transform-origin:0 0}
.phone{position:absolute;top:45px;width:218px;border:5px solid var(--frame);border-radius:30px;background:var(--screen);overflow:hidden}
.abs{position:absolute}
svg.ic{width:10px;height:10px;flex:none}
.search{position:absolute;left:14px;top:14px;width:160px;height:22px;border-radius:11px;background:var(--field);font-size:7px;color:var(--muted);display:flex;align-items:center;gap:5px;padding-left:8px}
.search svg{width:9px;height:9px;color:#555}
.menu{position:absolute;left:186px;top:19px;width:12px;height:12px;color:#333}
.headline{position:absolute;left:13px;top:70px;font-size:11px;font-weight:500;white-space:nowrap}
.headline em{font-style:normal;color:var(--pink)}
.row{position:absolute;left:12px;width:190px;height:24px;border-radius:12px;background:#fff;display:flex;align-items:center;gap:6px;padding:0 9px;font-size:6.6px;font-weight:500;color:var(--ink)}
.row .ic{color:var(--icon);width:9px;height:9px}
.row .label{flex:1;white-space:nowrap}
.row .chev{color:#333;width:9px;height:9px}
.row.narrow{width:160px}
.row.active{background:var(--grad);color:#fff}
.row.active .ic,.row.active .chev{color:#fff}
.row.sub{height:20px;border-radius:10px;font-size:5.8px;background:#e4e5e9}
.row.sub.active{background:var(--blue)}
.filter-btn{position:absolute;left:178px;width:24px;height:24px;border-radius:12px;background:#fff;display:flex;align-items:center;justify-content:center;color:#444}
.nav{position:absolute;left:0;right:0;display:flex;justify-content:space-around;padding:0 10px;font-size:6.6px;color:var(--muted);text-align:center}
.nav div{display:flex;flex-direction:column;align-items:center;gap:2px}
.nav svg{width:11px;height:11px;color:#9a9ca6}
.nav .on,.nav .on svg{color:var(--icon)}
.nav .on span{color:var(--blue)}
.dig{background:linear-gradient(135deg,#d9a06a,#b4652e 45%,#e2803a 60%,#9e6b44)}
.site{background:linear-gradient(135deg,#cfd6dd,#a9b3bb 40%,#d7c9ae 70%,#9aa7b2)}
.btn{position:absolute;display:flex;align-items:center;justify-content:center;border-radius:14px;font-size:7px;font-weight:500}
.btn.fill{background:var(--grad);color:#fff}
.btn.line{border:1px solid var(--blue);color:var(--blue);background:#fff}
.step{position:absolute;left:14px;width:176px;font-size:5.6px;color:var(--ink)}
.step .cap{display:flex;justify-content:space-between;align-items:center}
.step .cap svg{width:8px;height:8px}
.step .lesson{display:flex;justify-content:space-between;gap:4px;margin-top:10px;font-weight:500;white-space:nowrap}
.step .lesson small{font-size:5.4px;font-weight:400;color:var(--muted)}
.bar{height:2px;background:var(--track);margin-top:6px;border-radius:1px}
.bar i{display:block;height:100%;width:0;background:var(--blue);border-radius:1px}
.rail{position:absolute;left:7px;width:1px;background:#c9cbd2}
.dot{position:absolute;left:5px;width:5px;height:5px;border-radius:50%;background:#c9cbd2}
.dot.on{background:var(--icon)}
.field{position:absolute;left:17px;width:180px;height:27px;border-radius:14px;background:#fff;display:flex;align-items:center;gap:6px;padding-left:12px;font-size:7px;color:var(--ink)}
.field.ph-text{color:var(--muted)}
.field svg{width:8px;height:8px;color:#aaa}
.tile{position:absolute;width:93px;height:103px;background:#fff;border-radius:4px;padding:8px}
.tile svg{width:44px;height:36px;color:#333}
.tile p{font-size:9.5px;line-height:1.5;margin-top:20px;color:#333}
.lesson-card{position:absolute;left:8px;width:196px;height:110px;background:#fff;border-radius:3px;overflow:hidden}
.lesson-card .img{height:52px}
.lesson-card p{font-size:6.4px;line-height:1.65;padding:6px 8px 0;font-weight:500}
.lesson-card .actor{font-size:5.6px;font-weight:400;color:var(--muted);padding:2px 8px 0}
.actor b{color:var(--pink);font-weight:400}
.topbar{position:absolute;left:12px;top:14px;display:flex;align-items:center;gap:14px;font-size:10px;font-weight:500}
.back{width:22px;height:22px;border-radius:11px;background:#fff;display:flex;align-items:center;justify-content:center;color:#222}
.back svg{width:9px;height:9px}
.desc h4{font-size:7.4px;font-weight:700}
.desc p{font-size:6.6px;line-height:1.75;color:#444;margin-top:6px}
.attach{position:absolute;left:12px;width:195px;height:24px;border-radius:4px;background:#fff;display:flex;align-items:center;gap:6px;padding:0 9px;font-size:6.6px}
.attach .ic{color:var(--icon);width:9px;height:9px}
.attach .label{flex:1}
.attach .dl{color:var(--blue)}
.toggle{position:absolute;left:16px;display:flex;gap:10px;font-size:7px;color:#444;line-height:1.5}
.toggle .sw{flex:none;width:22px;height:12px;border-radius:6px;border:1px solid #c9cbd2;background:#fff;position:relative;margin-top:-1px}
.toggle .sw::after{content:"";position:absolute;left:1px;top:1px;width:8px;height:8px;border-radius:50%;background:#d8d9de}
.toggle.on{color:var(--blue)}
.toggle.on .sw{background:var(--blue);border-color:var(--blue)}
.toggle.on .sw::after{left:auto;right:1px;background:#fff}
.play{position:absolute;width:22px;height:22px;border-radius:50%;background:var(--pink);display:flex;align-items:center;justify-content:center;color:#fff}
.play svg{width:8px;height:8px}
.social-btn{color:var(--ink);gap:6px;font-size:8px;font-weight:500}
.social-btn .mark{width:8px;height:8px;background:var(--blue)}
</style>
</head>
<body>
<svg width="0" height="0" style="position:absolute">
  <defs>
    <symbol id="i-chart" viewBox="0 0 12 12"><rect x="1" y="6" width="2" height="5" fill="currentColor"/><rect x="5" y="2" width="2" height="9" fill="currentColor"/><rect x="9" y="4" width="2" height="7" fill="currentColor"/></symbol>
    <symbol id="i-list" viewBox="0 0 12 12"><rect x="1" y="1.5" width="10" height="2.3" fill="currentColor"/><rect x="1" y="5" width="10" height="2.3" fill="currentColor"/><rect x="1" y="8.5" width="10" height="2.3" fill="currentColor"/></symbol>
    <symbol id="i-grid" viewBox="0 0 12 12"><rect x="1" y="1" width="4.3" height="4.3" fill="currentColor"/><rect x="6.7" y="1" width="4.3" height="4.3" fill="currentColor"/><rect x="1" y="6.7" width="4.3" height="4.3" fill="currentColor"/><rect x="6.7" y="6.7" width="4.3" height="4.3" fill="currentColor"/></symbol>
    <symbol id="i-doc" viewBox="0 0 12 12"><rect x="1.5" y="2" width="9" height="9" rx="1" fill="none" stroke="currentColor" stroke-width="1.2"/><path d="M1.5 4.5h9M4 1v2M8 1v2" stroke="currentColor" stroke-width="1.2"/></symbol>
    <symbol id="i-cycle" viewBox="0 0 12 12"><path d="M10 5A4 4 0 0 0 2.6 3.5M2 7a4 4 0 0 0 7.4 1.5" fill="none" stroke="currentColor" stroke-width="1.3"/><path d="M2 1.5v2.5h2.5M10 10.5V8H7.5" fill="none" stroke="currentColor" stroke-width="1.3"/></symbol>
    <symbol id="i-up" viewBox="0 0 12 12"><polyline points="3,7.5 6,4.5 9,7.5" fill="none" stroke="currentColor" stroke-width="1.5"/></symbol>
    <symbol id="i-down" viewBox="0 0 12 12"><polyline points="3,4.5 6,7.5 9,4.5" fill="none" stroke="currentColor" stroke-width="1.5"/></symbol>
    <symbol id="i-search" viewBox="0 0 12 12"><circle cx="5" cy="5" r="3.5" fill="none" stroke="currentColor" stroke-width="1.4"/><path d="M7.6 7.6L11 11" stroke="currentColor" stroke-width="1.4"/></symbol>
    <symbol id="i-menu" viewBox="0 0 12 12"><path d="M1 2.5h10M1 6h10M4 9.5h7" stroke="currentColor" stroke-width="1.3"/></symbol>
    <symbol id="i-filter" viewBox="0 0 12 12"><path d="M1 3h10M1 6h10M1 9h10" stroke="currentColor" stroke-width=".9"/><circle cx="4" cy="3" r="1.2" fill="#fff" stroke="currentColor" stroke-width=".9"/><circle cx="8" cy="6" r="1.2" fill="#fff" stroke="currentColor" stroke-width=".9"/><circle cx="5" cy="9" r="1.2" fill="#fff" stroke="currentColor" stroke-width=".9"/></symbol>
    <symbol id="i-home" viewBox="0 0 12 12"><path d="M1 6L6 1.5 11 6v5H7.5V8h-3v3H1z" fill="currentColor"/></symbol>
    <symbol id="i-res" viewBox="0 0 12 12"><rect x="1" y="1.5" width="10" height="2.5" fill="currentColor"/><rect x="1" y="5" width="10" height="2.5" fill="currentColor"/><rect x="1" y="8.5" width="10" height="2.5" fill="currentColor"/></symbol>
    <symbol id="i-act" viewBox="0 0 12 12"><rect x="1.5" y="2" width="9" height="9" rx="1" fill="none" stroke="currentColor" stroke-width="1.1"/><path d="M1.5 4.5h9M4 1v2M8 1v2M3.5 6.5h1M5.5 6.5h1M7.5 6.5h1M3.5 8.5h1M5.5 8.5h1" stroke="currentColor" stroke-width="1"/></symbol>
    <symbol id="i-prof" viewBox="0 0 12 12"><circle cx="6" cy="3.8" r="2.6" fill="currentColor"/><path d="M1 11.5a5 4 0 0 1 10 0z" fill="currentColor"/></symbol>
    <symbol id="i-back" viewBox="0 0 12 12"><polyline points="7.5,2.5 4,6 7.5,9.5" fill="none" stroke="currentColor" stroke-width="1.6"/></symbol>
    <symbol id="i-next" viewBox="0 0 12 12"><polyline points="4.5,2.5 8,6 4.5,9.5" fill="none" stroke="currentColor" stroke-width="1.6"/></symbol>
    <symbol id="i-heart" viewBox="0 0 12 12"><path d="M6 10.5L1.6 6.2A2.6 2.6 0 0 1 6 2.8a2.6 2.6 0 0 1 4.4 3.4z" fill="currentColor"/></symbol>
    <symbol id="i-dl" viewBox="0 0 12 12"><path d="M6 1.5v8M2.5 6L6 9.5 9.5 6" fill="none" stroke="currentColor" stroke-width="1.3"/></symbol>
    <symbol id="i-play" viewBox="0 0 12 12"><path d="M3 1.5L10.5 6 3 10.5z" fill="currentColor"/></symbol>
    <symbol id="i-mail" viewBox="0 0 12 12"><rect x="1" y="2.5" width="10" height="7" fill="none" stroke="currentColor" stroke-width="1"/><path d="M1 2.5l5 4 5-4" fill="none" stroke="currentColor" stroke-width="1"/></symbol>
    <symbol id="i-lock" viewBox="0 0 12 12"><rect x="2" y="5.5" width="8" height="5.5" fill="currentColor"/><path d="M3.8 5.5V4a2.2 2.2 0 0 1 4.4 0v1.5" fill="none" stroke="currentColor" stroke-width="1.1"/></symbol>
    <symbol id="i-plan" viewBox="0 0 44 36"><path d="M3 4h4v28H3z M7 6h34v26H7" fill="none" stroke="currentColor" stroke-width="1.4"/><rect x="12" y="10" width="11" height="9" fill="none" stroke="currentColor" stroke-width="1.2"/><rect x="26" y="10" width="10" height="5" fill="none" stroke="#e667a6" stroke-width="1.2"/><rect x="12" y="22" width="6" height="6" fill="none" stroke="#e667a6" stroke-width="1.2"/><rect x="22" y="19" width="5" height="9" fill="none" stroke="currentColor" stroke-width="1.2"/><rect x="30" y="19" width="5" height="9" fill="none" stroke="currentColor" stroke-width="1.2"/></symbol>
  </defs>
</svg>

<main class="stage">

  <!-- Screen 1: Sign in -->
  <section class="phone" style="left:55px;height:467px">
    <div class="abs" role="img" aria-label="Illustration of construction engineers reviewing plans beside a crane" style="left:20px;top:18px;width:172px;height:120px;border-radius:6px;background:linear-gradient(160deg,#eef0f4,#c5ccd8 60%,#e9d8e6)"></div>
    <div class="abs" style="left:0;right:0;top:152px;text-align:center;font-size:20px;font-weight:700;letter-spacing:.5px;color:var(--ink)">VELMIRO</div>
    <div class="abs" style="left:0;right:0;top:183px;text-align:center;font-size:8px;line-height:1.7;color:var(--muted)">Welcome to Virtual<br>Engineering Leaders</div>
    <div class="field" style="top:238px"><svg><use href="#i-mail"/></svg>Example.mailbox.com</div>
    <div class="field ph-text" style="top:277px"><svg><use href="#i-lock"/></svg>Password</div>
    <div class="btn fill" style="left:17px;top:324px;width:180px;height:29px;font-size:8.5px">Login</div>
    <div class="abs" style="left:17px;top:367px;width:180px;height:1px;background:#d4d6dc"></div>
    <div class="abs" style="left:100px;top:362px;padding:0 3px;background:var(--screen);font-size:7px;color:var(--muted)">Or</div>
    <div class="btn line social-btn" style="left:17px;top:383px;width:180px;height:29px"><span class="mark"></span>Sign-up with Corvanet</div>
  </section>

  <!-- Screen 2: Home -->
  <section class="phone" style="left:322px;height:467px">
    <div class="search"><svg><use href="#i-search"/></svg>Search</div>
    <svg class="menu"><use href="#i-menu"/></svg>
    <div class="headline">Your <em>Velmiro</em> Journey Starts Here</div>
    <div class="row narrow" style="top:99px"><svg class="ic"><use href="#i-chart"/></svg><span class="label">Customize Your Journey</span></div>
    <div class="filter-btn" style="top:99px"><svg class="ic"><use href="#i-filter"/></svg></div>
    <div class="row" style="top:135px"><svg class="ic"><use href="#i-list"/></svg><span class="label">How To Start BIM?</span><svg class="chev"><use href="#i-up"/></svg></div>
    <div class="row" style="top:172px"><svg class="ic"><use href="#i-grid"/></svg><span class="label">Important ISO19650 Principles To Know</span><svg class="chev"><use href="#i-up"/></svg></div>
    <div class="row" style="top:208px"><svg class="ic"><use href="#i-list"/></svg><span class="label">Information Management Processes</span><svg class="chev"><use href="#i-up"/></svg></div>
    <div class="row" style="top:245px"><svg class="ic"><use href="#i-doc"/></svg><span class="label">Documents You Need To Develop</span><svg class="chev"><use href="#i-up"/></svg></div>
    <div class="row" style="top:281px"><svg class="ic"><use href="#i-cycle"/></svg><span class="label">Other Resources</span><svg class="chev"><use href="#i-up"/></svg></div>
    <nav class="nav" style="top:428px">
      <div class="on"><svg><use href="#i-home"/></svg><span>Home</span></div>
      <div><svg><use href="#i-res"/></svg><span>Resource</span></div>
      <div><svg><use href="#i-act"/></svg><span>Actifites</span></div>
      <div><svg><use href="#i-prof"/></svg><span>Profile</span></div>
    </nav>
  </section>

  <!-- Screen 3: Filter sheet -->
  <section class="phone" style="left:590px;height:467px;background:#9c9da1">
    <div class="search" style="background:#87888c;color:#6b6c70"><svg><use href="#i-search"/></svg>Search</div>
    <svg class="menu"><use href="#i-menu"/></svg>
    <div class="headline">Your <em style="color:#b2507f">Velmiro</em> Journey Starts Here</div>
    <div class="row narrow" style="top:99px;background:#a5a6aa"><svg class="ic" style="color:#3d4680"><use href="#i-chart"/></svg><span class="label">Customize Your Journey</span></div>
    <div class="filter-btn" style="top:99px;background:#a5a6aa"><svg class="ic"><use href="#i-filter"/></svg></div>
    <div class="row" style="top:135px;background:#a5a6aa"><svg class="ic" style="color:#3d4680"><use href="#i-list"/></svg><span class="label">How To Start BIM?</span><svg class="chev"><use href="#i-up"/></svg></div>
    <div class="row" style="top:172px;background:#a5a6aa"><svg class="ic" style="color:#3d4680"><use href="#i-grid"/></svg><span class="label">Important ISO19650 Principles To Know</span><svg class="chev"><use href="#i-up"/></svg></div>
    <div class="abs" style="left:0;right:0;top:200px;bottom:0;background:#fff;border-radius:10px 10px 0 0">
      <svg class="abs" style="right:10px;top:8px;width:9px;height:9px"><path d="M1 1l7 7M8 1L1 8" stroke="#222" stroke-width="1.3"/></svg>
      <div class="abs" style="left:16px;top:33px;font-size:10px;font-weight:500">Filter</div>
      <div class="toggle on" style="top:65px"><span class="sw"></span>Show All</div>
      <div class="toggle" style="top:90px"><span class="sw"></span>I Am The Client (Appointing Party)</div>
      <div class="toggle" style="top:115px"><span class="sw"></span>I Am The Lead Consultant/Contractor,&nbsp; Etc.</div>
      <div class="toggle" style="top:140px"><span class="sw"></span>I Am The Consultant/Subcontractor/<br>Supplier, Etc.</div>
    </div>
  </section>

  <!-- Screen 4: ISO principles tiles -->
  <section class="phone" style="left:858px;height:635px">
    <div class="search"><svg><use href="#i-search"/></svg>Search</div>
    <svg class="menu"><use href="#i-menu"/></svg>
    <div class="headline">Your <em>Velmiro</em> Journey Starts Here</div>
    <div class="row narrow" style="top:99px"><svg class="ic"><use href="#i-chart"/></svg><span class="label">Customize Your Journey</span></div>
    <div class="filter-btn" style="top:99px"><svg class="ic"><use href="#i-filter"/></svg></div>
    <div class="row" style="top:135px"><svg class="ic"><use href="#i-list"/></svg><span class="label">How To Start BIM?</span><svg class="chev"><use href="#i-up"/></svg></div>
    <div class="row active" style="top:172px"><svg class="ic"><use href="#i-grid"/></svg><span class="label">Important ISO19650 Principles To Know</span><svg class="chev"><use href="#i-down"/></svg></div>
    <div class="tile" style="left:12px;top:215px"><svg><use href="#i-plan"/></svg><p>PAS 1192 vs<br>ISO 19650</p><span class="abs" style="left:0;bottom:0;width:30px;height:3px;background:var(--blue)"></span></div>
    <div class="tile" style="left:111px;top:215px"><svg><use href="#i-plan"/></svg><p>Who are<br>the actors?</p></div>
    <div class="tile" style="left:12px;top:332px"><svg><use href="#i-plan"/></svg><p>Project level vs.<br>Appointment level</p></div>
    <div class="tile" style="left:111px;top:332px"><svg><use href="#i-plan"/></svg><p>Information<br>Stages</p></div>
    <div class="row" style="top:455px"><svg class="ic"><use href="#i-list"/></svg><span class="label">Information Management Processes</span><svg class="chev"><use href="#i-up"/></svg></div>
    <div class="row" style="top:491px"><svg class="ic"><use href="#i-doc"/></svg><span class="label">Documents You Need To Develop</span><svg class="chev"><use href="#i-up"/></svg></div>
    <div class="row" style="top:528px"><svg class="ic"><use href="#i-cycle"/></svg><span class="label">Other Resources</span><svg class="chev"><use href="#i-up"/></svg></div>
    <nav class="nav" style="top:595px">
      <div class="on"><svg><use href="#i-home"/></svg><span>Home</span></div>
      <div><svg><use href="#i-res"/></svg><span>Resource</span></div>
      <div><svg><use href="#i-act"/></svg><span>Actifites</span></div>
      <div><svg><use href="#i-prof"/></svg><span>Profile</span></div>
    </nav>
  </section>

  <!-- Screen 5: Information management processes -->
  <section class="phone" style="left:1127px;height:597px">
    <div class="search"><svg><use href="#i-search"/></svg>Search</div>
    <svg class="menu"><use href="#i-menu"/></svg>
    <div class="headline">Your <em>Velmiro</em> Journey Starts Here</div>
    <div class="row narrow" style="top:99px"><svg class="ic"><use href="#i-chart"/></svg><span class="label">Customize Your Journey</span></div>
    <div class="filter-btn" style="top:99px"><svg class="ic"><use href="#i-filter"/></svg></div>
    <div class="row" style="top:135px"><svg class="ic"><use href="#i-list"/></svg><span class="label">How To Start BIM?</span><svg class="chev"><use href="#i-up"/></svg></div>
    <div class="row" style="top:172px"><svg class="ic"><use href="#i-grid"/></svg><span class="label">Important ISO19650 Principles To Know</span><svg class="chev"><use href="#i-up"/></svg></div>
    <div class="row active" style="top:208px"><svg class="ic"><use href="#i-list"/></svg><span class="label">Information Management Processes</span><svg class="chev"><use href="#i-down"/></svg></div>
    <div class="row sub active" style="top:252px;color:#fff"><span class="label">Project Level (Early Stage)</span><svg class="chev" style="color:#fff"><use href="#i-down"/></svg></div>
    <span class="dot on" style="top:294px"></span>
    <div class="step" style="top:291px;left:20px;width:175px">
      <div class="cap"><span>(Information Requirement Stage)</span><svg><use href="#i-down"/></svg></div>
      <div class="lesson" style="margin-top:12px"><span>5.1 Assessment &amp; Need</span><small>Progress 10%</small></div>
      <div class="bar"><i style="width:10%"></i></div>
    </div>
    <div class="btn fill" style="left:18px;top:342px;width:62px;height:19px;font-size:6px">Explore</div>
    <div class="btn line" style="left:92px;top:342px;width:62px;height:19px;font-size:6px">View All</div>
    <div class="row sub" style="top:380px"><span class="label">Appointment Level</span><svg class="chev"><use href="#i-up"/></svg></div>
    <div class="row sub" style="top:414px"><span class="label">Project Level (Close Our Stage)</span><svg class="chev"><use href="#i-up"/></svg></div>
    <div class="row" style="top:452px"><svg class="ic"><use href="#i-doc"/></svg><span class="label">Documents You Need To Develop</span><svg class="chev"><use href="#i-up"/></svg></div>
    <div class="row" style="top:489px"><svg class="ic"><use href="#i-cycle"/></svg><span class="label">Other Resources</span><svg class="chev"><use href="#i-up"/></svg></div>
    <nav class="nav" style="top:556px">
      <div class="on"><svg><use href="#i-home"/></svg><span>Home</span></div>
      <div><svg><use href="#i-res"/></svg><span>Resource</span></div>
      <div><svg><use href="#i-act"/></svg><span>Actifites</span></div>
      <div><svg><use href="#i-prof"/></svg><span>Profile</span></div>
    </nav>
  </section>

  <!-- Screen 6: Lesson list -->
  <section class="phone" style="left:1395px;height:570px">
    <div class="topbar"><span class="back"><svg><use href="#i-back"/></svg></span>5.1 Assessment &amp; Need</div>
    <article class="lesson-card" style="top:70px"><div class="img dig" role="img" aria-label="Excavator working on a construction site"></div><p>5.1.1 Appoint individuals to undertake information management function</p><div class="actor"><b>Actor:</b> The Appointing Party</div></article>
    <article class="lesson-card" style="top:191px"><div class="img dig" role="img" aria-label="Excavator working on a construction site"></div><p>5.1.1 Appoint individuals to undertake information management function</p><div class="actor"><b>Actor:</b> The Appointing Party</div></article>
    <article class="lesson-card" style="top:312px"><div class="img dig" role="img" aria-label="Excavator working on a construction site"></div><p>5.1.1 Appoint individuals to undertake information management function</p><div class="actor"><b>Actor:</b> The Appointing Party</div></article>
    <article class="lesson-card" style="top:433px"><div class="img dig" role="img" aria-label="Excavator working on a construction site"></div><p>5.1.1 Appoint individuals to undertake information management function</p><div class="actor"><b>Actor:</b> The Appointing Party</div></article>
  </section>

  <!-- Screen 7: Appointment level stages -->
  <section class="phone" style="left:1663px;height:880px">
    <div class="search"><svg><use href="#i-search"/></svg>Search</div>
    <svg class="menu"><use href="#i-menu"/></svg>
    <div class="headline">Your <em>Velmiro</em> Journey Starts Here</div>
    <div class="row narrow" style="top:99px"><svg class="ic"><use href="#i-chart"/></svg><span class="label">Customize Your Journey</span></div>
    <div class="filter-btn" style="top:99px"><svg class="ic"><use href="#i-filter"/></svg></div>
    <div class="row" style="top:135px"><svg class="ic"><use href="#i-list"/></svg><span class="label">How To Start BIM?</span><svg class="chev"><use href="#i-up"/></svg></div>
    <div class="row" style="top:172px"><svg class="ic"><use href="#i-grid"/></svg><span class="label">Important ISO19650 Principles To Know</span><svg class="chev"><use href="#i-up"/></svg></div>
    <div class="row active" style="top:208px"><svg class="ic"><use href="#i-list"/></svg><span class="label">Information Management Processes</span><svg class="chev"><use href="#i-down"/></svg></div>
    <div class="row sub" style="top:252px"><span class="label">Project Level (Early Stage)</span><svg class="chev"><use href="#i-up"/></svg></div>
    <div class="row sub active" style="top:286px;color:#fff"><span class="label">Appointment Level</span><svg class="chev" style="color:#fff"><use href="#i-up"/></svg></div>
    <span class="rail" style="top:330px;height:325px"></span>
    <span class="dot on" style="top:327px"></span>
    <div class="step" style="top:324px;left:20px"><div class="cap"><span>Information Requirement Stage 2</span><svg><use href="#i-down"/></svg></div><div class="lesson"><span>5.2 Invitation To Tender</span><small>Progress 10%</small></div><div class="bar"><i style="width:42%"></i></div></div>
    <div class="btn fill" style="left:18px;top:375px;width:62px;height:19px;font-size:6px">Explore</div>
    <div class="btn line" style="left:92px;top:375px;width:62px;height:19px;font-size:6px">View All</div>
    <span class="dot" style="top:414px"></span>
    <div class="step" style="top:411px;left:20px"><div class="cap"><span>Information Requirement Stage 3</span><svg><use href="#i-up"/></svg></div><div class="lesson"><span>5.3 Tender Response</span><small>Progress 0%</small></div><div class="bar"></div></div>
    <span class="dot" style="top:471px"></span>
    <div class="step" style="top:468px;left:20px"><div class="cap"><span>Information Planning Stage 1</span><svg><use href="#i-up"/></svg></div><div class="lesson"><span>5.4 Appointment</span><small>Progress 0%</small></div><div class="bar"></div></div>
    <span class="dot" style="top:528px"></span>
    <div class="step" style="top:525px;left:20px"><div class="cap"><span>Information Planning Stage 2</span><svg><use href="#i-up"/></svg></div><div class="lesson"><span>5.5 Mobilization</span><small>Progress 0%</small></div><div class="bar"></div></div>
    <span class="dot" style="top:585px"></span>
    <div class="step" style="top:582px;left:20px"><div class="cap"><span>Information Delivery Stage 1</span><svg><use href="#i-up"/></svg></div><div class="lesson"><span>5.6 Collaborative Production Of Information</span><small>Progress 0%</small></div><div class="bar"></div></div>
    <span class="dot" style="top:642px"></span>
    <div class="step" style="top:639px;left:20px"><div class="cap"><span>Information Delivery Stage 2</span><svg><use href="#i-up"/></svg></div><div class="lesson"><span>5.7 Information Model Delivery</span><small>Progress 0%</small></div><div class="bar"></div></div>
    <div class="row sub" style="top:698px"><span class="label">Project Level (Close Our Stage)</span><svg class="chev"><use href="#i-up"/></svg></div>
    <div class="row" style="top:737px"><svg class="ic"><use href="#i-doc"/></svg><span class="label">Documents You Need To Develop</span><svg class="chev"><use href="#i-up"/></svg></div>
    <div class="row" style="top:774px"><svg class="ic"><use href="#i-cycle"/></svg><span class="label">Other Resources</span><svg class="chev"><use href="#i-up"/></svg></div>
    <nav class="nav" style="top:840px">
      <div class="on"><svg><use href="#i-home"/></svg><span>Home</span></div>
      <div><svg><use href="#i-res"/></svg><span>Resource</span></div>
      <div><svg><use href="#i-act"/></svg><span>Actifites</span></div>
      <div><svg><use href="#i-prof"/></svg><span>Profile</span></div>
    </nav>
  </section>

  <!-- Screen 8: Video description -->
  <section class="phone" style="left:1935px;height:570px">
    <div class="topbar"><span class="back"><svg><use href="#i-back"/></svg></span><span style="margin-left:22px">Video Description</span></div>
    <div class="abs" style="left:12px;top:72px;font-size:6.6px;color:var(--pink)">Appointment Level</div>
    <svg class="abs" style="left:194px;top:71px;width:10px;height:10px;color:#d8466f"><use href="#i-heart"/></svg>
    <div class="abs" style="left:12px;top:88px;width:195px;font-size:9.6px;font-weight:500;line-height:1.6">5.1.1 Appoint Individuals To Undertake The Information Management Function</div>
    <div class="abs" style="left:12px;top:131px;font-size:6.6px;color:#555">(Information Procurement Stage)</div>
    <div class="abs actor" style="left:12px;top:146px;font-size:6.6px;color:#555"><b>Actor:</b> The Lead Appointed Party</div>
    <div class="abs site" role="img" aria-label="Video still of engineers in hard hats on a building site" style="left:12px;top:178px;width:195px;height:112px"></div>
    <div class="play" style="left:98px;top:223px"><svg><use href="#i-play"/></svg></div>
    <div class="abs desc" style="left:12px;top:313px;width:190px"><h4>Description :</h4><p>Lorem ipsum dolor sit amet, consetetur ing elitr, sed diam nonumy eirmod tempor invidunt ut labore et dolore magna aliquyam erat, sed diam</p></div>
    <div class="btn fill" style="left:144px;top:392px;width:62px;height:19px;font-size:6.4px">Start →</div>
    <div class="abs" style="left:12px;top:447px;font-size:8px;font-weight:500">Attachment</div>
    <div class="attach" style="top:469px"><svg class="ic"><use href="#i-doc"/></svg><span class="label">Lorem Ipsum Ser Dolor Amet</span><svg class="ic dl"><use href="#i-dl"/></svg></div>
    <div class="attach" style="top:506px"><svg class="ic"><use href="#i-cycle"/></svg><span class="label">Lorem Ipsum Ser Dolor Amet</span><svg class="ic dl"><use href="#i-dl"/></svg></div>
  </section>

  <!-- Screen 9: Lesson player -->
  <section class="phone" style="left:2207px;height:467px">
    <div class="abs" style="left:0;right:0;top:0;height:168px;background:linear-gradient(160deg,var(--purple),#8e6fbc 45%,var(--blue));border-radius:0 0 22px 22px"></div>
    <span class="abs back" style="left:12px;top:14px"><svg><use href="#i-back"/></svg></span>
    <div class="abs" style="left:9px;top:59px;font-size:6.6px;color:#fff">Appointment Level</div>
    <div class="abs" style="left:9px;top:75px;width:198px;font-size:9.6px;font-weight:500;line-height:1.6;color:#fff">5.1.1 Appoint Individuals To Undertake The Information Management Function</div>
    <div class="abs" style="left:9px;top:118px;font-size:6.6px;color:#fff">(Information Procurement Stage)</div>
    <div class="abs" style="left:9px;top:133px;font-size:6.6px;color:#fff"><b style="font-weight:500">Actor:</b> The Lead Appointed Party</div>
    <div class="abs site" role="img" aria-label="Video still of engineers in hard hats on a building site" style="left:9px;top:188px;width:195px;height:122px"></div>
    <div class="play" style="left:95px;top:238px"><svg><use href="#i-play"/></svg></div>
    <div class="abs desc" style="left:9px;top:337px;width:192px"><h4>Description :</h4><p>Lorem ipsum dolor sit amet, consetetur ing elitr, sed diam nonumy eirmod tempor invidunt ut labore et dolore magna aliquyam erat, sed diam</p></div>
    <div class="abs" style="left:0;right:0;top:440px;height:1px;background:#e1e2e6"></div>
    <div class="abs" style="left:0;right:0;top:445px;display:flex;justify-content:center;align-items:center;gap:4px;font-size:9px;color:var(--blue)">
      <svg style="width:8px;height:8px"><use href="#i-back"/></svg><b style="font-weight:700">02</b><span style="color:var(--muted)">/ 06</span><svg style="width:8px;height:8px"><use href="#i-next"/></svg>
    </div>
    <svg class="abs" style="left:190px;top:446px;width:10px;height:10px;color:#d8466f"><use href="#i-heart"/></svg>
  </section>

</main>
</body>
</html>
```